Consultative Employee Benifits Firm Needs Business Card Design Project

We need a business card design for a new company based in Northern Virginia called "Tallow Ridge Advisors, LLC. We are both a wealth management advisory firm, as well as an employee benefits firm, which strives to provide superior creativity in employee benefits plan design and greater client and employee satisfaction. We are obsessed with service and follow up.

Our firm specializes in the areas of group health, life, dental, disability, voluntary benefits, Executive Benefits, HRA and HSA programs. We offer competitive employee benefit packages and pricing models for single or multi-state/multi location companies by maintaining preferred relationships with a large number of regional and national carriers.

Our firm also considers the many dimensions of your wealth through an integrated process we call wealth structuring — a comprehensive, dynamic approach to building, preserving, enjoying and transferring your wealth. And because we are often dealing with complex ownership structures and complicated, changing family dynamics, we bring the highest level of experience and creativity to managing your wealth. We work hard to help ensure that your legacy lasts by preparing your children for the financial challenges and opportunities that are headed their way.

Our final design should communicate an integrated approach to finanial safety and optimization
Updates

 Due to a few designers not accepting due to low budget, I have increased budget payout 19%. 

Project Deadline Extended
Reason: I have only heard from 12 designers. So, maybe I did not give the right amount of time to do the project. For the designers that have submitted their designs, thank you. I have seen three or four designs that I liked and might end up with one of them after it's all over, but I thought I would see between 20 - 25 before everything was over. Dean

Target Market(s)

Professionals; doctors, contractors, small to mid size business owners, ages 50 -65 with nert worth of 2MM

Industry/Entity Type

Financial

Requirements
Must have
• Tallow Ridge Advisors, LLC

Dean Harlow
President
17459 Marrowind Lane Street
Quenby Hollow, 20418

Office: 703 562-1094
Cell: 703 817-2650
Fax: 703 275-6831
Email: deanharlow@mailtrove.net
Should not have
• No pink or yellow colors.
No generic clipart (coins, dollar signs, money bags, graphs)

```html
<!DOCTYPE html>
<html lang="en">
<head>
<meta charset="utf-8">
<title>Tallow Ridge Advisors, LLC — Business Card</title>
<link rel="stylesheet" href="https://fonts.googleapis.com/css2?family=Questrial&family=Open+Sans:wght@400&display=swap">
<style>
  :root {
    --backdrop: #e4e5e7;
    --card: #000000;
    --accent: #1ab8e8;
    --ink-light: #ffffff;
  }
  * { margin: 0; padding: 0; box-sizing: border-box; }
  html, body {
    width: 1199px;
    height: 1200px;
    overflow: hidden;
    background: var(--backdrop);
  }
  .stage {
    position: relative;
    width: 1199px;
    height: 1200px;
  }
  .card {
    position: absolute;
    width: 458px;
    height: 252px;
    background: var(--card);
    font-family: "Questrial", sans-serif;
  }
  .card--front {
    left: 81px;
    top: 450px;
    border-bottom-left-radius: 54px;
  }
  .card--back {
    left: 652px;
    top: 454px;
    border-bottom-right-radius: 54px;
  }
  .brand-mark {
    position: absolute;
    left: 203px;
    top: 502px;
    left: 203px;
  }
  .brand-square {
    position: absolute;
    left: 205px;
    top: 46px;
    width: 48px;
    height: 48px;
  }
  .brand-name {
    position: absolute;
    left: 0;
    right: 0;
    top: 153px;
    text-align: center;
    color: var(--accent);
    font-size: 27px;
    letter-spacing: 0.2px;
    white-space: nowrap;
  }
  .holder-name {
    position: absolute;
    left: 34px;
    top: 34px;
    color: var(--accent);
    font-size: 32px;
    letter-spacing: -0.3px;
    white-space: nowrap;
  }
  .holder-title {
    position: absolute;
    left: 113px;
    top: 74px;
    color: var(--ink-light);
    font-family: "Open Sans", sans-serif;
    font-size: 14px;
  }
  .contact-list {
    position: absolute;
    left: 234px;
    top: 147px;
    list-style: none;
    font-size: 9.5px;
    line-height: 13.5px;
    white-space: nowrap;
  }
  .contact-label { color: var(--ink-light); }
  .contact-label::first-letter { font-size: 12px; }
  .contact-value { color: var(--accent); }
  .contact-indent { display: block; padding-left: 43px; }
</style>
</head>
<body>
  <main class="stage">
    <section class="card card--front" aria-label="Card front">
      <svg class="brand-square" viewBox="0 0 48 48" aria-hidden="true">
        <rect x="2" y="2" width="44" height="44" fill="none" stroke="#1ab8e8" stroke-width="4"/>
      </svg>
      <p class="brand-name">Tallow Ridge Advisors LLC</p>
    </section>

    <section class="card card--back" aria-label="Card back">
      <h1 class="holder-name">Dean Harlow</h1>
      <p class="holder-title">President</p>
      <ul class="contact-list">
        <li><span class="contact-label">Address:</span> <span class="contact-value">17459 Marrowind Lane Street</span>
          <span class="contact-value contact-indent">Quenby Hollow, 20418</span></li>
        <li><span class="contact-label">Office No:</span> <span class="contact-value">703-562-1094</span></li>
        <li><span class="contact-label">Cell No:</span> <span class="contact-value">703-817-2650</span></li>
        <li><span class="contact-label">Fax No:</span> <span class="contact-value">703 275-6831</span></li>
        <li><span class="contact-label">Email id:</span> <span class="contact-value">deanharlow@mailtrove.net</span></li>
      </ul>
    </section>
  </main>
</body>
</html>
```